Velvet Harbor (A luxury Travel Website)

website text attached in document below

images also attached

feel free to use other images if needed

Target Market(s)

Luxury Seekers and wealthy couples / families

Industry/Entity Type

Luxury Travel

Coding

Coded - Design and coding required

Number of Pages Required

1 page

Requirements
Must have
• A luxury design and easy use.
Nice to have
• Ease of use of page, incorporation of images into the flow of the site

```html
<!DOCTYPE html>
<html lang="en">
<head>
<meta charset="utf-8">
<title>Velvet Harbor — Luxury Travel</title>
<link href="https://fonts.googleapis.com/css2?family=Cinzel:wght@400;500&family=Roboto:wght@400;500;700&display=swap" rel="stylesheet">
<style>
:root{
  --sky:#8cc4ee;
  --sky-soft:#a9d3f3;
  --accent:#7dbbea;
  --ink:#111111;
  --text:#222222;
  --muted:#6d6d6d;
  --gold:#d4a33c;
  --footer:#1b1b1b;
  --white:#ffffff;
}
*{box-sizing:border-box;margin:0;padding:0}
html,body{width:1200px;height:4137px;overflow:hidden}
body{position:relative;font-family:'Roboto',sans-serif;color:var(--text);background:var(--white)}
.abs{position:absolute}
.serif{font-family:'Cinzel',serif;font-variant:small-caps}

/* top bar */
.topbar{left:0;top:0;width:1200px;height:42px;background:var(--sky)}
.topbar span{position:absolute;top:14px;font-size:12px;font-weight:500;color:var(--white);letter-spacing:.3px;display:flex;align-items:center;gap:7px}
.topbar svg{width:11px;height:11px;fill:var(--white)}

/* nav */
.nav{left:0;top:42px;width:1200px;height:66px;background:var(--ink)}
.brand{position:absolute;font-family:'Cinzel',serif;font-size:31px;letter-spacing:1px;color:var(--sky);white-space:nowrap}
.nav .brand{left:111px;top:13px}
.nav a{position:absolute;top:24px;font-size:15px;font-weight:700;color:var(--white);text-decoration:none}
.nav a.active{color:var(--sky)}

/* hero */
.hero{left:0;top:108px;width:1200px;height:684px;background:linear-gradient(180deg,#3f77b8 0%,#7fb2d9 30%,#4fc4c9 55%,#2fb0b3 75%,#7a8f8c 100%)}
.hero h1{position:absolute;left:0;width:1200px;top:70px;text-align:center;font-weight:500;font-size:48px;color:var(--white);text-shadow:0 2px 6px rgba(0,0,0,.45)}
.booking{left:210px;top:633px;width:781px;height:122px;border-radius:22px;background:rgba(255,255,255,.55)}
.booking label{position:absolute;top:25px;font-size:12px;font-weight:700;color:var(--ink)}
.field{position:absolute;top:51px;width:174px;height:47px;background:var(--white);border:1px solid #d8d8d8;font-size:9px;color:#555;padding:0 12px;display:flex;align-items:center;justify-content:space-between}
.field i{width:0;height:0;border-left:4px solid transparent;border-right:4px solid transparent;border-top:4px solid #333}
.booking .check{position:absolute;left:582px;top:51px;width:173px;height:45px;background:var(--sky);color:var(--white);font-size:13px;font-weight:700;display:flex;align-items:center;justify-content:center;border-radius:3px}

/* about */
.about-frame{left:128px;top:901px;width:450px;height:381px;background:var(--sky)}
.about-img{left:116px;top:888px;width:441px;height:373px;background:linear-gradient(135deg,#1c8fa2,#2bb2bf 50%,#167e92);border:3px solid var(--white)}
.rule{position:absolute;width:50px;height:3px;background:var(--sky)}
.about h2{position:absolute;left:641px;top:982px;width:480px;font-size:31px;font-weight:400;line-height:43px;color:var(--ink)}
.about p{position:absolute;left:641px;top:1132px;width:455px;font-size:15px;line-height:23px;color:var(--muted);text-align:justify}

/* plans band */
.plans{left:0;top:1400px;width:1200px;height:322px;background:linear-gradient(180deg,#9ccbf0,#8cc4ee)}
.plans h2{position:absolute;left:0;top:72px;width:1200px;text-align:center;font-size:31px;font-weight:400;line-height:43px;color:var(--white)}
.input{position:absolute;top:201px;height:52px;background:var(--white);border-radius:2px;font-size:15px;font-weight:500;color:var(--ink);padding:0 18px;display:flex;align-items:center;justify-content:space-between}
.input svg{width:13px;height:13px;fill:var(--ink)}
.submit{position:absolute;left:900px;top:201px;width:166px;height:52px;background:var(--ink);color:var(--white);font-size:14px;font-weight:700;display:flex;align-items:center;justify-content:center;border-radius:2px}

/* section titles */
.title{position:absolute;left:0;width:1200px;text-align:center;font-size:34px;font-weight:400;color:var(--ink)}

/* hotels */
.card{position:absolute;top:1918px;width:316px}
.card-img{height:263px;border-radius:16px 16px 0 0;position:relative}
.rating{position:absolute;left:22px;top:22px;width:52px;height:22px;border-radius:11px;background:var(--gold);color:var(--white);font-size:11px;font-weight:700;display:flex;align-items:center;justify-content:center;gap:3px}
.heart{position:absolute;right:36px;bottom:-12px;width:26px;height:26px;border-radius:50%;background:var(--white);display:flex;align-items:center;justify-content:center;box-shadow:0 1px 3px rgba(0,0,0,.2)}
.heart svg{width:13px;height:13px;fill:var(--accent)}
.card h3{margin:20px 0 0 32px;font-size:18px;font-weight:700;color:var(--ink)}
.card p{margin:24px 12px 0 32px;font-size:12.5px;line-height:19px;color:var(--muted);text-align:justify}
.price{margin:11px 0 0 32px;font-size:21px;font-weight:700;color:var(--accent)}
.price small{font-size:13px;font-weight:500}
.learn{margin:10px 0 0 32px;font-size:12px;font-weight:500;color:var(--accent);text-decoration:underline;display:flex;align-items:center;gap:8px}
.learn b{width:11px;height:11px;border-radius:50%;background:var(--accent);display:inline-block}
.dots{left:567px;top:2419px;display:flex;gap:5px}
.dots i{width:9px;height:9px;border-radius:50%;background:var(--accent)}
.dots i.off{background:var(--white);border:1px solid var(--accent)}

/* direct */
.direct{left:0;top:2473px;width:1200px;height:574px;background:linear-gradient(180deg,#ffffff 0%,#f1f6f9 35%,#d7e5ee 52%,#4f8aa8 56%,#c9d2d6 66%,#e9edef 100%)}
.direct h2{position:absolute;left:0;top:62px;width:1200px;text-align:center;font-size:31px;font-weight:400;line-height:43px;color:var(--ink)}
.direct p{position:absolute;left:110px;top:166px;width:980px;text-align:center;font-size:15px;line-height:23px;color:var(--muted)}

/* gallery */
.gallery{left:111px;top:3226px;display:grid;grid-template-columns:repeat(4,236px);grid-auto-rows:193px;gap:13px 11px}

/* footer */
.footer{left:0;top:3726px;width:1200px;height:361px;background:var(--footer)}
.footer .brand{left:111px;top:167px}
.footer h4{position:absolute;top:82px;font-size:13px;font-weight:700;color:var(--white)}
.footer .line{position:absolute;top:104px;height:1px;background:#777}
.flink{position:absolute;font-size:13px;color:var(--white);display:flex;align-items:center;gap:14px}
.flink::before{content:"»";font-size:13px}
.news{position:absolute;left:801px;top:137px;font-size:13px;color:var(--white)}
.email{position:absolute;left:801px;top:164px;width:286px;height:47px;background:var(--white);border-radius:3px;font-size:13px;color:#666;padding:0 17px;display:flex;align-items:center}
.send{position:absolute;right:0;top:0;width:44px;height:47px;background:var(--sky);border-radius:0 3px 3px 0;display:flex;align-items:center;justify-content:center}
.send svg{width:15px;height:15px;fill:var(--white)}
.social{position:absolute;top:240px;width:36px;height:36px;border:1px solid var(--white);border-radius:50%}
.social::after{content:"";position:absolute;left:14px;top:14px;width:6px;height:6px;border-radius:50%;background:var(--white)}
.copy{left:0;top:4087px;width:1200px;height:50px;background:var(--sky);color:var(--white);font-size:13px}
.copy span{position:absolute;top:18px}
</style>
</head>
<body>

<header>
  <div class="abs topbar">
    <span style="left:112px"><svg viewBox="0 0 12 12"><circle cx="6" cy="6" r="6"/><path d="M3 6l2 2 4-4" stroke="#8cc4ee" stroke-width="1.6" fill="none"/></svg>LOYALTY</span>
    <span style="left:233px"><svg viewBox="0 0 12 12"><path d="M2 1h8v3a4 4 0 0 1-8 0zM5 8h2v2h2v2H3v-2h2z"/></svg>BEST RATE GUARANTEE</span>
    <span style="left:438px"><svg viewBox="0 0 12 12"><path d="M2 0h8v12L6 9 2 12z"/></svg>MY BOOKING</span>
    <span style="left:825px"><svg viewBox="0 0 12 12"><path d="M0 5h6V2l5 4-5 4V7H0z"/></svg>LOG IN</span>
    <span style="left:936px"><svg viewBox="0 0 12 12"><circle cx="6" cy="3.5" r="3"/><path d="M0 12a6 5 0 0 1 12 0z"/></svg>SIGN UP</span>
    <span style="left:1050px"><svg viewBox="0 0 12 12"><path d="M2 4h8L6 9z"/></svg>INR</span>
  </div>
  <nav class="abs nav">
    <div class="brand">Velvet Harbor</div>
    <a class="active" href="#" style="left:479px">Home</a>
    <a href="#" style="left:562px">About Us</a>
    <a href="#" style="left:668px">Our Hotels</a>
    <a href="#" style="left:784px">Festive Journey</a>
    <a href="#" style="left:936px">Gallery</a>
    <a href="#" style="left:1028px">Contact</a>
  </nav>
</header>

<section class="abs hero" role="img" aria-label="Couple walking along a wooden jetty over a turquoise lagoon towards a thatched overwater hut">
  <h1 class="serif">Maldive's Best Luxury Deals</h1>
</section>
<form class="abs booking">
  <label style="left:24px">Check In - Check Out *</label>
  <label style="left:211px">Guests *</label>
  <label style="left:396px">Hotel Name *</label>
  <div class="field" style="left:24px">02/11/2022 - 04/11/2022<svg width="9" height="9" viewBox="0 0 9 9"><rect width="9" height="9" fill="#555"/><rect x="1" y="3" width="7" height="5" fill="#fff"/></svg></div>
  <div class="field" style="left:211px">0 Persons<i></i></div>
  <div class="field" style="left:396px">Hotel Name<i></i></div>
  <div class="check">CHECK AVAILABILITY</div>
</form>

<section class="about">
  <div class="abs about-frame"></div>
  <div class="abs about-img" role="img" aria-label="Aerial view of overwater villas arranged in a curve over a reef lagoon"></div>
  <div class="rule" style="left:641px;top:966px"></div>
  <h2 class="serif">Looking to stay at a 5 star hotel or to fly business class anywhere?</h2>
  <p>Sed ut perspiciatis unde omnis iste natus error sit voluptatem accusantium doloremque laudantium, totam rem aperiam, eaque ipsa quae ab illo inventore veritatis</p>
</section>

<section class="abs plans" role="img" aria-label="Faint palm trees on a sky blue background">
  <h2 class="serif">Tell us about your next holiday plans.<br>The more details the better.</h2>
  <div class="input" style="left:128px;width:372px">Name<svg viewBox="0 0 12 12"><circle cx="6" cy="3.5" r="3"/><path d="M1 12a5 5 0 0 1 10 0z"/></svg></div>
  <div class="input" style="left:515px;width:371px">Message<svg viewBox="0 0 14 12"><ellipse cx="7" cy="5" rx="6" ry="4" fill="none" stroke="#111" stroke-width="1.4"/><path d="M3 8l-1 3 4-2"/></svg></div>
  <div class="submit">SUBMIT NOW</div>
</section>

<section class="hotels">
  <div class="rule" style="left:575px;top:1811px"></div>
  <h2 class="title serif" style="top:1828px">Our Hotels</h2>

  <article class="card" style="left:111px">
    <div class="card-img" role="img" aria-label="Hotel bedroom with white bed and leafy mural wall" style="background:linear-gradient(180deg,#b9c1b6,#8f9d8c 55%,#e9e8e6)">
      <div class="rating">4.5 ★</div>
      <div class="heart"><svg viewBox="0 0 12 11"><path d="M6 11L1 6a3 3 0 0 1 5-4 3 3 0 0 1 5 4z"/></svg></div>
    </div>
    <h3>Lorem ipsum dolor sit</h3>
    <p>Sed ut perspiciatis unde omnis iste natus error sit voluptatem accusantium doloreIaudantium, totam rem aperiam, eaque ipsa</p>
    <div class="price">$50.00 <small>/ 2 Nights</small></div>
    <div class="learn">LEARN MORE <b></b></div>
  </article>

  <article class="card" style="left:442px">
    <div class="card-img" role="img" aria-label="Business class airline suite with reclining seat" style="background:linear-gradient(180deg,#d9cfc7,#8b6a5c 55%,#4a2c28)">
      <div class="rating">4.5 ★</div>
      <div class="heart"><svg viewBox="0 0 12 11"><path d="M6 11L1 6a3 3 0 0 1 5-4 3 3 0 0 1 5 4z"/></svg></div>
    </div>
    <h3>Lorem ipsum dolor sit</h3>
    <p>Sed ut perspiciatis unde omnis iste natus error sit voluptatem accusantium doloreIaudantium, totam rem aperiam, eaque ipsa</p>
    <div class="price">$50.00 <small>/ 2 Nights</small></div>
    <div class="learn">LEARN MORE <b></b></div>
  </article>

  <article class="card" style="left:773px">
    <div class="card-img" role="img" aria-label="Resort villa lit at dusk beside a pool and palm trees" style="background:linear-gradient(180deg,#4a7bc0,#6a8fb8 40%,#b8683a 70%,#3a5f86)">
      <div class="rating">4.5 ★</div>
      <div class="heart"><svg viewBox="0 0 12 11"><path d="M6 11L1 6a3 3 0 0 1 5-4 3 3 0 0 1 5 4z"/></svg></div>
    </div>
    <h3>Lorem ipsum dolor sit</h3>
    <p>Sed ut perspiciatis unde omnis iste natus error sit voluptatem accusantium doloreIaudantium, totam rem aperiam, eaque ipsa</p>
    <div class="price">$50.00 <small>/ 2 Nights</small></div>
    <div class="learn">LEARN MORE <b></b></div>
  </article>

  <div class="abs dots"><i class="off"></i><i></i><i></i><i></i><i></i></div>
</section>

<section class="abs direct" role="img" aria-label="Sun loungers and lanterns on a white deck facing the sea under a pale sky">
  <div class="rule" style="left:575px;top:39px"></div>
  <h2 class="serif">We work directly with hotels and airlines to<br>get you the best price, always.</h2>
  <p>Sed ut perspiciatis unde omnis iste natus error sit voluptatem accusantium doloremque laudantium, totam rem aperiam, eaque ipsa quae ab illo inventore veritatis et quasi architecto beatae vitae dicta sunt explicabo. Nemo enim ipsam voluptatem quia voluptas sit aspernatur aut odit aut fugit, sed quia consequuntur magni dolores eos qui ratione voluptatem sequi nesciunt.</p>
</section>

<section class="gallery-section">
  <div class="rule" style="left:575px;top:3131px"></div>
  <h2 class="title serif" style="top:3150px">Our Gallery</h2>
  <div class="abs gallery">
    <div role="img" aria-label="Infinity pool terrace with loungers over the sea" style="background:linear-gradient(180deg,#4f8fd0,#e8e4de)"></div>
    <div role="img" aria-label="Bright hotel bedroom with chandelier" style="background:linear-gradient(180deg,#e6e3df,#7b818a)"></div>
    <div role="img" aria-label="Modern lounge with white armchairs" style="background:linear-gradient(180deg,#3b3a38,#d9d5cf)"></div>
    <div role="img" aria-label="Minimal bedroom with large windows" style="background:linear-gradient(180deg,#d3d4d4,#6d6b69)"></div>
    <div role="img" aria-label="Warm lit hotel bedroom with patterned rug" style="background:linear-gradient(180deg,#c9b39a,#5c4538)"></div>
    <div role="img" aria-label="Villa pool surrounded by tropical garden" style="background:linear-gradient(180deg,#6f9a5a,#bfd9dc 60%,#3f9fb4)"></div>
    <div role="img" aria-label="Glass walled living room overlooking the sea" style="background:linear-gradient(180deg,#a9cbe6,#eef1f3)"></div>
    <div role="img" aria-label="Beach with rows of straw umbrellas beside a resort pool" style="background:linear-gradient(180deg,#3a6ea8,#6aa9c4 45%,#c7a36a)"></div>
  </div>
</section>

<footer class="abs footer">
  <div class="brand">Velvet Harbor</div>
  <h4 style="left:426px">LINKS</h4>
  <div class="line" style="left:426px;width:296px"></div>
  <a class="flink" style="left:426px;top:124px">Home</a>
  <a class="flink" style="left:426px;top:158px">About us</a>
  <a class="flink" style="left:426px;top:193px">Properties</a>
  <a class="flink" style="left:426px;top:228px">Our Gallery</a>
  <a class="flink" style="left:426px;top:262px">Contact</a>
  <a class="flink" style="left:605px;top:124px">FAQ</a>
  <a class="flink" style="left:605px;top:158px">Our Hotels</a>
  <a class="flink" style="left:605px;top:193px">Privacy Policy</a>
  <a class="flink" style="left:605px;top:228px">Terms Of Use</a>
  <a class="flink" style="left:605px;top:262px">Help Service</a>
  <h4 style="left:801px">NEWSLETTER</h4>
  <div class="line" style="left:801px;width:280px"></div>
  <div class="news">Send us a newsletter to get update</div>
  <div class="email">Email Address<div class="send"><svg viewBox="0 0 16 16"><path d="M0 7L16 0 12 16 8 10z"/></svg></div></div>
  <div class="social" style="left:803px"></div>
  <div class="social" style="left:846px"></div>
  <div class="social" style="left:889px"></div>
  <div class="social" style="left:932px"></div>
</footer>
<div class="abs copy">
  <span style="left:111px">© 2022 Velvet Harbor . All Rights Reserved</span>
  <span style="left:918px">✉&nbsp; stay@velvetharbor.travel</span>
  <span style="left:1144px;font-size:10px;top:20px">C42</span>
</div>

</body>
</html>
```